Copper Meadow Creamery Business cards

We need a logo design for our family dairy. Included on the cards should be my name/my husbands name/the dairy name/ all the phone numbers/address and email. The name is Copper Meadow Creamery, LLC. We would like to use our farm mascot pic on the card. We know the pictures I sent you are of a beef cow but she is the mascot of the farm. We were thinking that maybe put a picture of her head in the middle of the card with a "B" on one side and a "D" on the other side with a "C" around the picture of the cow. But we are open to any ideas. We are looking for something kind of professional and a design that that can be used on cards, clothing and a car sign. Black lettering and blue for the other color...or what looks good.

Target Market(s)

All

Industry/Entity Type

Farming

Contact Information for Business Card

Marla Dutton Owner (555)417-2093
Ronald Pfister Owner (555)238-7715
Copper Meadow Creamery, LLC (555)906-4182
Coppermeadowcreamery@mailbarn.test
7126 County Lane 91, Brookvale, IA 50917

Font styles to use
Sans Serif

Colors
3176b5
3c7bb8
3277b5
0255a3

Requirements
Must have
• Some design that incorporates a drawing/pic of the cow pictures that were sent.
Nice to have
• no suggestions
Should not have
• no suggestions

```html
<!DOCTYPE html>
<html lang="en">
<head>
<meta charset="utf-8">
<title>Copper Meadow Creamery – Business Card</title>
<link rel="stylesheet" href="https://fonts.googleapis.com/css2?family=Barlow:wght@500;600&display=swap">
<style>
  :root {
    --brand-blue: #2e3796;
    --accent-blue: #1f7fc4;
    --ink: #111111;
    --meadow-light: #d9ea7a;
    --meadow-mid: #9cc83c;
    --meadow-deep: #4f8f1c;
    --grass: #3f9a1a;
    --milk: #f4f4ee;
    --white: #ffffff;
  }
  * { box-sizing: border-box; margin: 0; padding: 0; }
  html, body { width: 1200px; height: 667px; overflow: hidden; background: #ffffff; }
  .card {
    position: relative;
    width: 1200px;
    height: 667px;
    overflow: hidden;
    font-family: "Barlow", "Helvetica Neue", Arial, sans-serif;
    color: var(--ink);
  }
  .meadow-backdrop {
    position: absolute; inset: 0;
    background: radial-gradient(ellipse at 55% 35%, var(--meadow-light) 0%, var(--meadow-mid) 45%, var(--meadow-deep) 100%);
  }
  .grass-strip {
    position: absolute; left: 0; right: 0; bottom: 0; height: 130px;
    background: linear-gradient(180deg, rgba(90,170,40,0) 0%, var(--grass) 45%, #2f7d12 100%);
  }
  .milk-still-life {
    position: absolute; left: 620px; top: 150px; width: 580px; height: 460px;
    background: radial-gradient(ellipse at 60% 55%, var(--milk) 0%, rgba(244,244,238,0.75) 40%, rgba(244,244,238,0) 72%);
  }
  .art-layer { position: absolute; inset: 0; width: 1200px; height: 667px; }
  .logo-name {
    position: absolute;
    right: 60px; top: 40px;
    width: 620px;
    color: var(--white);
    font-weight: 600;
    font-size: 60px;
    line-height: 62px;
    text-align: right;
  }
  .logo-name span { display: block; }
  .contact { position: absolute; left: 387px; }
  .contact--first { top: 296px; }
  .contact--second { top: 448px; }
  .contact-name { font-size: 48px; font-weight: 500; line-height: 54px; letter-spacing: 0.5px; white-space: nowrap; }
  .contact-role { font-size: 20px; font-weight: 500; letter-spacing: 0.5px; }
  .contact-phone { font-size: 31px; font-weight: 500; line-height: 38px; letter-spacing: 2.5px; white-space: nowrap; }
  .main-phone {
    position: absolute; right: 32px; top: 548px;
    font-size: 50px; font-weight: 500; letter-spacing: 3px; line-height: 56px; white-space: nowrap;
  }
  .email {
    position: absolute; right: 32px; top: 614px;
    font-size: 22px; font-weight: 500; letter-spacing: 0.5px; white-space: nowrap;
  }
  .address {
    position: absolute; left: 36px; top: 611px;
    font-size: 27px; font-weight: 500; letter-spacing: 1px; white-space: nowrap;
  }
</style>
</head>
<body>
  <div class="card">
    <div class="meadow-backdrop" role="img" aria-label="Soft-focus green meadow background"></div>
    <div class="milk-still-life" role="img" aria-label="Glass pitcher and glass of milk beside a metal milk can"></div>
    <div class="grass-strip" role="img" aria-label="Fresh green grass along the bottom edge"></div>

    <svg class="art-layer" viewBox="0 0 1200 667">
      <defs>
        <clipPath id="mascot-clip"><circle cx="85" cy="124" r="254"/></clipPath>
        <linearGradient id="mascot-tone" x1="0" y1="0" x2="1" y2="1">
          <stop offset="0" stop-color="#3a3a3a"/>
          <stop offset="0.45" stop-color="#e9e9e6"/>
          <stop offset="1" stop-color="#9cc83c"/>
        </linearGradient>
      </defs>
      <circle class="mascot-ring" cx="107" cy="164" r="282" fill="var(--brand-blue)"/>
      <g role="img" aria-label="Portrait of the farm's mascot cow">
        <rect x="-200" y="-150" width="560" height="540" clip-path="url(#mascot-clip)" fill="url(#mascot-tone)"/>
      </g>
      <path class="banner-stripe" fill="var(--accent-blue)"
        d="M560 248 C700 228 1000 188 1200 160 L1200 180 C1000 204 720 242 585 254 Z"/>
      <path class="banner" fill="var(--brand-blue)"
        d="M500 246 C466 214 462 128 522 82 C600 22 800 12 1200 0 L1200 164 C1000 180 820 200 700 216 C620 226 560 240 500 246 Z"/>
    </svg>

    <div class="logo-name">
      <span>Copper Meadow</span>
      <span>Creamery, LLC</span>
    </div>

    <div class="contact contact--first">
      <div class="contact-name">Marla Dutton <span class="contact-role">(Owner)</span></div>
      <div class="contact-phone">(555)417-2093</div>
    </div>

    <div class="contact contact--second">
      <div class="contact-name">Ronald Pfister <span class="contact-role">(Owner)</span></div>
      <div class="contact-phone">(555)238-7715</div>
    </div>

    <div class="main-phone">(555)906-4182</div>
    <div class="email">coppermeadowcreamery@mailbarn.test</div>
    <div class="address">7126 County Lane 91, Brookvale, IA 50917</div>
  </div>
</body>
</html>
```